Birchmoor Yard Care_2015 New Cards_V1

We need an enhanced business card from what we have today. We are a Landscaping company and we have an existing Logo and text info that we would like to include.
Text to include:
In business for over 20 years,Fully Insured, Weekly Lawn Maintenance, Spring & Fall Clean-up, Todd Pierson, 203-555-0147, www.birchmooryardcarect.example, Visit our Website for additional Lawn Care Services or email directly at TODD@BIRCHMOORYARDCARE.EXAMPLE, We appreciate your business.
We want full color background and we will want to take this design and work with a printer that does high graphic silk screen cards. The colors we have thought about are Black, with our Green Logo, with Gold Text...we are open to different colors, we just want the card to wow!

Target Market(s)

Lawn Care Maintenance

Industry/Entity Type

Lawn Care

Contact Information for Business Card

Text to include:
In business for over 20 years, Fully Insured, Weekly Lawn Maintenance, Spring & Fall Clean-up, Todd Pierson, 203-555-0147, www.birchmooryardcarect.example, Visit our Website for additional Lawn Care Services or email directly at TODD@BIRCHMOORYARDCARE.EXAMPLE, We appreciate your business.

Requirements
Must have
• Logo, text details about how to reach us, standard size business cards that go horizontal.
Nice to have
• background colors, background designs, raised embossed lettering, rounded corners(2 or 4),

```html
<!DOCTYPE html>
<html lang="en">
<head>
<meta charset="utf-8">
<title>Birchmoor Yard Care – Business Card</title>
<link rel="stylesheet" href="https://fonts.googleapis.com/css2?family=Questrial&display=swap">
<style>
  :root {
    --stage: #e9ebe6;
    --cream: #f1efe2;
    --green-deep: #0f4a14;
    --green-mid: #1f6a1f;
    --green-bright: #2e8a2a;
    --green-accent: #5fb23a;
    --ink: #2e2e2a;
    --cream-text: #efeedd;
  }
  * { box-sizing: border-box; margin: 0; padding: 0; }
  html, body { width: 1200px; height: 786px; overflow: hidden; }
  body {
    background: var(--stage);
    font-family: "Questrial", "Century Gothic", sans-serif;
    position: relative;
  }
  .card {
    position: absolute;
    top: 238px;
    width: 540px;
    height: 309px;
    border-radius: 16px;
    overflow: hidden;
    box-shadow: 0 6px 18px rgba(0,0,0,.18);
  }
  .card--front { left: 40px; background: var(--cream); color: var(--ink); }
  .card--back {
    left: 620px;
    background: linear-gradient(160deg, var(--green-deep) 0%, var(--green-mid) 55%, var(--green-bright) 100%);
    color: var(--cream-text);
    text-align: center;
  }

  /* Front */
  .wordmark {
    position: absolute;
    font-size: 26px;
    letter-spacing: .04em;
    text-transform: uppercase;
    line-height: 1.1;
  }
  .card--front .wordmark { left: 34px; top: 34px; width: 240px; color: var(--green-deep); }
  .services {
    position: absolute;
    left: 34px; top: 132px;
    font-size: 13px;
    line-height: 1.55;
    color: var(--ink);
  }
  .contact {
    position: absolute;
    left: 292px; top: 40px;
  }
  .contact__name {
    font-size: 17px;
    color: var(--green-bright);
    text-transform: uppercase;
    letter-spacing: .04em;
    margin-bottom: 10px;
  }
  .contact__line {
    display: flex; align-items: center; gap: 8px;
    font-size: 12.5px;
    line-height: 1.9;
  }
  .contact__icon {
    width: 15px; height: 15px; flex: none;
    border-radius: 3px;
    background: var(--green-bright);
  }
  .lawn-band { position: absolute; left: 0; bottom: 0; width: 540px; height: 130px; }

  /* Back */
  .card--back .wordmark {
    position: static;
    margin: 74px auto 0;
    font-size: 34px;
    color: var(--cream-text);
  }
  .back__web { margin-top: 18px; font-size: 14px; }
  .back__web span { color: var(--green-accent); }
  .back__note { margin: 14px auto 0; width: 420px; font-size: 13px; line-height: 1.5; }
</style>
</head>
<body>

<section class="card card--front" aria-label="Card front">
  <div class="wordmark">Birchmoor Yard Care</div>

  <p class="services">
    In business for over 20 years · Fully Insured<br>
    Weekly Lawn Maintenance · Spring &amp; Fall Clean-up
  </p>

  <div class="contact">
    <p class="contact__name">Todd Pierson</p>
    <p class="contact__line">
      <svg class="contact__icon" viewBox="0 0 16 16" aria-hidden="true"><rect width="16" height="16" rx="3" fill="#2e8a2a"/><path d="M5 3.5l2 2-1 1.3c.6 1.3 1.6 2.3 2.9 2.9l1.3-1 2 2-1.2 1.5C8 12 4 8 3.8 4.7z" fill="#f1efe2"/></svg>
      203-555-0147
    </p>
    <p class="contact__line">
      <svg class="contact__icon" viewBox="0 0 16 16" aria-hidden="true"><rect width="16" height="16" rx="3" fill="#2e8a2a"/><rect x="3" y="4.5" width="10" height="7" fill="none" stroke="#f1efe2" stroke-width="1.2"/><path d="M3 4.5l5 4 5-4" fill="none" stroke="#f1efe2" stroke-width="1.2"/></svg>
      todd@birchmooryardcare.example
    </p>
    <p class="contact__line">
      <svg class="contact__icon" viewBox="0 0 16 16" aria-hidden="true"><rect width="16" height="16" rx="3" fill="#2e8a2a"/><circle cx="8" cy="8" r="4.6" fill="none" stroke="#f1efe2" stroke-width="1.1"/><path d="M3.4 8h9.2M8 3.4c-2.4 2.6-2.4 6.6 0 9.2M8 3.4c2.4 2.6 2.4 6.6 0 9.2" fill="none" stroke="#f1efe2" stroke-width="1"/></svg>
      www.birchmooryardcarect.example
    </p>
  </div>

  <svg class="lawn-band" viewBox="0 0 540 130" preserveAspectRatio="none" role="img" aria-label="Green lawn band with a grass edge sweeping across the lower card">
    <defs>
      <linearGradient id="lawnFill" x1="0" y1="0" x2="0" y2="1">
        <stop offset="0" stop-color="#1f6a1f"/>
        <stop offset="1" stop-color="#0f4a14"/>
      </linearGradient>
    </defs>
    <path d="M0 20 C120 40 260 110 540 104 L540 130 L0 130 Z" fill="url(#lawnFill)"/>
    <path d="M0 30 C140 55 280 112 540 112" fill="none" stroke="#5fb23a" stroke-width="4"/>
  </svg>
</section>

<section class="card card--back" aria-label="Card back">
  <div class="wordmark">Birchmoor Yard Care</div>
  <p class="back__web">www.<span>birchmooryardcarect</span>.example</p>
  <p class="back__note">
    Visit our website for additional Lawn Care Services or email
    directly at todd@birchmooryardcare.example We appreciate your business.
  </p>
</section>

</body>
</html>
```